KR business cards
Business cards for Consulting outfit
Project: KR business cards
KR business cards -
Creative Brief
Professional
No name
No address
info@vosk-lantern.example
vosk-lantern.example
Would like business cards for 8 different people. No address on the card
Logo + We define the standard

```html
<!DOCTYPE html>
<html lang="en">
<head>
<meta charset="utf-8">
<title>vosk-lantern stationery</title>
<link rel="stylesheet" href="https://fonts.googleapis.com/css2?family=Cormorant+Garamond:wght@400;600&display=swap">
<style>
  :root {
    --backdrop: #8d8d8d;
    --paper: #ffffff;
    --red-deep: #a3161f;
    --red-bright: #d9343c;
    --ink: #4a4a4a;
    --ink-soft: #7a7a7a;
  }
  * { margin: 0; padding: 0; box-sizing: border-box; }
  html, body { width: 1200px; height: 626px; overflow: hidden; }
  body {
    background: var(--backdrop);
    font-family: "Cormorant Garamond", Georgia, serif;
    color: var(--ink);
    position: relative;
  }
  .piece { position: absolute; background: var(--paper); overflow: hidden; }
  .band { position: absolute; left: 0; right: 0; background: linear-gradient(90deg, var(--red-deep), var(--red-bright) 50%, var(--red-deep)); }
  .rule { position: absolute; left: 0; right: 0; height: 2px; background: var(--red-deep); }

  .brand { position: absolute; left: 0; right: 0; text-align: center; }
  .brand-mark {
    display: block; font-weight: 600; color: var(--red-deep);
    line-height: 1; letter-spacing: 1px;
  }
  .brand-name { display: block; font-weight: 400; color: var(--ink); line-height: 1; margin-top: 4px; }

  .small-text {
    position: absolute; left: 0; right: 0; text-align: center;
    font-size: 7px; color: var(--ink-soft); letter-spacing: .2px;
  }

  /* business card front */
  .card-front { left: 34px; top: 197px; width: 182px; height: 98px; }
  .card-front .brand { top: 20px; }
  .card-front .brand-mark { font-size: 22px; }
  .card-front .brand-name { font-size: 16px; }
  .card-front .small-text { top: 76px; }

  /* business card back */
  .card-back { left: 34px; top: 307px; width: 182px; height: 106px; }
  .card-back .person { position: absolute; top: 6px; left: 0; right: 0; text-align: center; font-size: 7px; line-height: 1.25; color: var(--ink); }
  .card-back .brand { top: 26px; }
  .card-back .brand-mark { font-size: 16px; }
  .card-back .brand-name { font-size: 13px; margin-top: 2px; }
  .card-back .band { bottom: 0; height: 40px; }
  .card-back .rule { bottom: 42px; height: 1px; }
  .card-back .contact { position: absolute; left: 0; right: 0; bottom: 6px; text-align: center; font-size: 6.5px; line-height: 1.45; color: #fff; }

  /* letterhead */
  .letterhead { left: 233px; top: 29px; width: 434px; height: 571px; }
  .letterhead .band.top { top: 0; height: 12px; }
  .letterhead .rule.top { top: 14px; }
  .letterhead .brand { top: 24px; }
  .letterhead .brand-mark { font-size: 30px; }
  .letterhead .brand-name { font-size: 22px; }
  .letterhead .small-text { bottom: 36px; }
  .letterhead .band.bottom { bottom: 0; height: 20px; }
  .letterhead .rule.bottom { bottom: 22px; }

  /* envelope back */
  .envelope-back { left: 679px; top: 77px; width: 478px; height: 211px; }
  .envelope-back svg { position: absolute; inset: 0; }

  /* envelope front */
  .envelope-front { left: 679px; top: 336px; width: 478px; height: 211px; }
  .envelope-front .band.top { top: 0; height: 15px; }
  .envelope-front .rule.top { top: 17px; }
  .envelope-front .brand { top: 36px; }
  .envelope-front .brand-mark { font-size: 26px; }
  .envelope-front .brand-name { font-size: 20px; }
  .envelope-front .small-text { bottom: 26px; }
</style>
</head>
<body>

  <section class="piece card-front" aria-label="Business card front">
    <div class="brand">
      <span class="brand-mark">KR</span>
      <span class="brand-name">vosk-lantern</span>
    </div>
    <p class="small-text">We define the standard</p>
  </section>

  <section class="piece card-back" aria-label="Business card back">
    <p class="person">Full Name<br>Consultant</p>
    <div class="brand">
      <span class="brand-mark">KR</span>
      <span class="brand-name">vosk-lantern</span>
    </div>
    <div class="rule"></div>
    <div class="band"></div>
    <p class="contact">Tel +000 000 0000<br>info@vosk-lantern.example<br>vosk-lantern.example</p>
  </section>

  <section class="piece letterhead" aria-label="Letterhead">
    <div class="band top"></div>
    <div class="rule top"></div>
    <div class="brand">
      <span class="brand-mark">KR</span>
      <span class="brand-name">vosk-lantern</span>
    </div>
    <p class="small-text">Tel +000 000 0000 &nbsp;·&nbsp; info@vosk-lantern.example &nbsp;·&nbsp; vosk-lantern.example</p>
    <div class="rule bottom"></div>
    <div class="band bottom"></div>
  </section>

  <section class="piece envelope-back" aria-label="Envelope back">
    <svg width="478" height="211" viewBox="0 0 478 211">
      <defs>
        <linearGradient id="flap-fill" x1="0" y1="0" x2="1" y2="0">
          <stop offset="0" stop-color="var(--red-deep)"/>
          <stop offset="0.5" stop-color="var(--red-bright)"/>
          <stop offset="1" stop-color="var(--red-deep)"/>
        </linearGradient>
      </defs>
      <path d="M0 0 H478 V8 L262 136 Q239 148 216 136 L0 8 Z" fill="url(#flap-fill)"/>
    </svg>
  </section>

  <section class="piece envelope-front" aria-label="Envelope front">
    <div class="band top"></div>
    <div class="rule top"></div>
    <div class="brand">
      <span class="brand-mark">KR</span>
      <span class="brand-name">vosk-lantern</span>
    </div>
    <p class="small-text">Tel +000 000 0000 &nbsp;·&nbsp; info@vosk-lantern.example &nbsp;·&nbsp; vosk-lantern.example</p>
  </section>

</body>
</html>
```